Modern Business Card for Lanternfield 2018

Our company assumes the best about people. We are creating an online community of entrepreneurs and business leaders who struggle with marketing their business online.

This business card should POP! We recently got a new logo and are launching a new website next month, so our business cards should make a statement that feels:
-Fresh
-Smart
-Trustworthy
-Fun

Target Market(s)

small business owners, entrepreneurs

Industry/Entity Type

Digital Marketing

Contact Information for Business Card

Dimensions: 3.5" x 2"

Font styles to use
Sans Serif

Colors
f37122
ffffff

Requirements
Must have
• We need a business card with a modern, bold design. We will use one side of the card as a lead-generation offer, so text on one side will need to fit up to 140 characters. The business card should stick to our core colors (orange, black, and white).
Nice to have
• We think a vertical "portrait" design could be interesting.
Should not have
• Should not look like a traditional business card. The round icon should stand out from a distance.

```html
<!DOCTYPE html>
<html lang="en">
<head>
<meta charset="utf-8">
<title>Lanternfield Business Card</title>
<link rel="stylesheet" href="https://fonts.googleapis.com/css2?family=Work+Sans:wght@400;500;800&family=Roboto+Condensed:wght@400&display=swap">
<style>
  :root {
    --orange: #f37122;
    --orange-deep: #c9531a;
    --ink: #2b2a29;
    --white: #ffffff;
    --paper: #f4f4f4;
    --mist: #d9d9d9;
    --stage: #e6e6e6;
  }
  html, body {
    margin: 0;
    width: 1200px;
    height: 900px;
    overflow: hidden;
    background: var(--stage);
    font-family: "Work Sans", sans-serif;
  }
  .canvas {
    position: relative;
    width: 1200px;
    height: 900px;
  }
  .card {
    position: absolute;
    left: 320px;
    width: 560px;
    height: 320px;
    border-radius: 18px;
    overflow: hidden;
    box-shadow: 0 10px 26px rgba(0,0,0,0.18);
  }

  /* Front */
  .card-front {
    top: 60px;
    background: linear-gradient(135deg, var(--white) 0%, var(--paper) 100%);
  }
  .front-brand {
    position: absolute;
    left: 36px;
    top: 40px;
    display: flex;
    align-items: flex-start;
    gap: 8px;
  }
  .brand-name {
    font-weight: 800;
    font-size: 38px;
    letter-spacing: 0.5px;
    color: var(--ink);
    line-height: 1;
    text-transform: uppercase;
  }
  .brand-dot {
    width: 22px;
    height: 22px;
    border-radius: 50%;
    background: var(--orange);
    margin-top: -14px;
  }
  .front-rule {
    position: absolute;
    left: 36px;
    right: 36px;
    top: 112px;
    height: 1px;
    background: #7a7a7a;
  }
  .contact-list {
    position: absolute;
    left: 36px;
    top: 130px;
    margin: 0;
    padding: 0;
    list-style: none;
    font-size: 15px;
    color: var(--ink);
  }
  .contact-list li {
    display: flex;
    align-items: center;
    gap: 8px;
    margin-bottom: 6px;
  }
  .contact-list svg { width: 11px; height: 11px; flex: none; }
  .web-accent { color: var(--orange); }
  .person {
    position: absolute;
    right: 36px;
    top: 150px;
    text-align: left;
    width: 230px;
  }
  .person-name {
    margin: 0;
    font-weight: 500;
    font-size: 24px;
    letter-spacing: 1px;
    color: var(--orange);
    text-transform: uppercase;
  }
  .person-title {
    margin: 2px 0 8px;
    font-size: 15px;
    color: var(--ink);
  }
  .person-rule {
    height: 1px;
    background: #7a7a7a;
    margin-bottom: 10px;
  }
  .person-address {
    margin: 0;
    font-style: normal;
    font-size: 14px;
    line-height: 1.35;
    color: var(--ink);
  }
  .front-base {
    position: absolute;
    left: 0;
    bottom: 0;
    width: 560px;
    height: 60px;
  }

  /* Back */
  .card-back {
    top: 520px;
    background: radial-gradient(circle at 30% 70%, #ee6a24 0%, var(--orange-deep) 100%);
    color: var(--mist);
    text-align: center;
  }
  .map-field {
    position: absolute;
    left: 60px;
    top: 30px;
    width: 440px;
    height: 250px;
    border-radius: 40px;
    background: radial-gradient(ellipse at center, rgba(255,255,255,0.10) 0%, rgba(255,255,255,0) 70%);
  }
  .back-brand {
    position: relative;
    margin-top: 52px;
    display: inline-flex;
    align-items: flex-start;
    gap: 10px;
  }
  .back-brand .brand-name {
    font-size: 54px;
    color: var(--mist);
  }
  .back-brand .brand-dot {
    width: 34px;
    height: 34px;
    background: var(--mist);
    margin-top: -24px;
  }
  .offer {
    position: relative;
    margin: 14px 0 0;
    font-family: "Roboto Condensed", sans-serif;
    font-size: 17px;
    line-height: 1.3;
    color: var(--white);
  }
  .back-rule {
    position: relative;
    margin: 12px auto 10px;
    width: 470px;
    height: 1px;
    background: rgba(255,255,255,0.7);
  }
  .slogan {
    position: relative;
    margin: 0;
    font-family: "Roboto Condensed", sans-serif;
    font-size: 17px;
    letter-spacing: 0.3px;
    color: var(--white);
    text-transform: uppercase;
  }
</style>
</head>
<body>
<main class="canvas">

  <section class="card card-front" aria-label="Card front">
    <div class="front-brand">
      <span class="brand-name">Lanternfield</span>
      <span class="brand-dot"></span>
    </div>
    <div class="front-rule"></div>

    <ul class="contact-list">
      <li>
        <svg viewBox="0 0 12 12"><path d="M3 1 L5 3.5 L4 5 Q5.5 7 7 8 L8.5 7 L11 9 L9.5 11 Q5 10.5 1.5 5 Q1 3 3 1Z" fill="var(--orange)"/></svg>
        (555) 310-4827
      </li>
      <li>
        <svg viewBox="0 0 12 12"><rect x="1" y="2.5" width="10" height="7" fill="none" stroke="var(--orange)" stroke-width="1.2"/><path d="M1 2.5 L6 6.5 L11 2.5" fill="none" stroke="var(--orange)" stroke-width="1.2"/></svg>
        mara@lanternfieldhq.com
      </li>
      <li>
        <svg viewBox="0 0 12 12"><circle cx="6" cy="6" r="5" fill="var(--orange)"/><path d="M1 6 H11 M6 1 Q3 6 6 11 M6 1 Q9 6 6 11" fill="none" stroke="var(--white)" stroke-width="0.8"/></svg>
        <span>www.<span class="web-accent">lanternfieldhq</span>.com</span>
      </li>
    </ul>

    <div class="person">
      <h1 class="person-name">Mara Ellison</h1>
      <p class="person-title">Story Marketing Coach</p>
      <div class="person-rule"></div>
      <address class="person-address">QZ2040, 48 Maplewood Row,<br>Norvale City, Westmark</address>
    </div>

    <svg class="front-base" viewBox="0 0 560 60" preserveAspectRatio="none">
      <path d="M0 30 L200 46 L560 46 L560 60 L0 60 Z" fill="var(--orange)"/>
      <path d="M0 38 L195 52 Q215 54 225 40 Q232 30 250 30 L560 30 L560 60 L0 60 Z" fill="var(--ink)"/>
    </svg>
  </section>

  <section class="card card-back" aria-label="Card back">
    <div class="map-field" role="img" aria-label="Faint dotted world map texture"></div>
    <div class="back-brand">
      <span class="brand-name">Lanternfield</span>
      <span class="brand-dot"></span>
    </div>
    <p class="offer">Get your free Lanternfield<br>Starter Package and our marketing guide today at</p>
    <div class="back-rule"></div>
    <p class="slogan">Reach more people. Make more money. Create more impact.</p>
  </section>

</main>
</body>
</html>
```